Chiropractor needs a snazzy business card

Business card for a chiropractic office.
Office treats patients of all ages.
Focus is on a natural lifestyle.
Colors can include the logo colors as well as white and a little orange.
Ideally the card would have something chiropractic related such as a spine.

The back of the card should have a items for making appointments (date, times....)

```html
<!DOCTYPE html>
<html lang="en">
<head>
<meta charset="utf-8">
<title>Meridian Chiropractic – Business Card</title>
<link href="https://fonts.googleapis.com/css2?family=Open+Sans:wght@400;600;700&display=swap" rel="stylesheet">
<style>
  :root {
    --navy: #1f4e7e;
    --green: #4cb748;
    --ink: #333333;
    --rule: #9a9a9a;
    --paper: #ffffff;
    --backdrop: #e9e6e1;
  }
  * { box-sizing: border-box; margin: 0; padding: 0; }
  html, body { width: 1200px; height: 1024px; overflow: hidden; }
  body {
    background: var(--backdrop);
    font-family: "Open Sans", Arial, sans-serif;
    position: relative;
  }
  .card {
    position: absolute;
    width: 720px;
    height: 410px;
    background: var(--paper);
    box-shadow: 0 6px 18px rgba(0,0,0,0.18);
    overflow: hidden;
  }
  /* Front */
  .card--front { left: 60px; top: 60px; }
  .front__band {
    position: absolute; left: 0; bottom: 0;
    width: 100%; height: 48px;
    background: var(--green);
  }
  .front__tab {
    position: absolute; right: 0; bottom: 0;
    width: 190px; height: 66px;
    background: var(--navy);
    color: var(--paper);
    font-size: 15px;
    display: flex; align-items: center; justify-content: center;
  }
  .front__brand {
    position: absolute; left: 56px; top: 96px;
    color: var(--navy);
    font-weight: 600;
    font-size: 46px;
    line-height: 1.05;
    letter-spacing: 1px;
    text-transform: uppercase;
  }
  .front__person {
    position: absolute; left: 56px; top: 228px;
    font-size: 22px; font-weight: 700; color: var(--navy);
  }
  .front__person .role { color: var(--green); font-weight: 600; font-size: 18px; }
  .front__person .sep { color: var(--ink); font-weight: 400; margin: 0 4px; }
  .contact-list { position: absolute; left: 56px; top: 264px; list-style: none; }
  .contact-list li {
    display: flex; align-items: center; gap: 10px;
    font-size: 19px; color: var(--ink); line-height: 28px;
  }
  .contact-list svg { width: 16px; height: 16px; fill: var(--green); }

  /* Back */
  .card--back { left: 420px; top: 560px; }
  .back__band {
    position: absolute; left: 0; bottom: 0;
    width: 100%; height: 44px;
    background: var(--green);
    border-top: 5px solid var(--navy);
    color: var(--paper);
    font-size: 14px;
    padding-left: 30px;
    display: flex; align-items: center;
  }
  .back__title {
    position: absolute; right: 60px; top: 40px;
    font-size: 22px; color: var(--ink); letter-spacing: 1px;
  }
  .appt-fields { position: absolute; left: 40px; top: 110px; width: 640px; }
  .appt-row { display: flex; gap: 30px; margin-bottom: 44px; }
  .appt-field {
    flex: 1; display: flex; align-items: flex-end; gap: 6px;
    font-size: 14px; color: var(--ink); letter-spacing: 0.5px;
  }
  .appt-field .line { flex: 1; border-bottom: 1px solid var(--rule); height: 16px; }
</style>
</head>
<body>

<section class="card card--front" aria-label="Business card front">
  <div class="front__brand">Meridian<br>Chiropractic</div>
  <p class="front__person">Daniel Marsh <span class="sep">|</span><span class="role">Chiropractor</span></p>
  <ul class="contact-list">
    <li><svg viewBox="0 0 16 16" aria-hidden="true"><path d="M3 1h3l1.5 4-2 1.3a9 9 0 0 0 4.2 4.2L11 8.5l4 1.5v3a2 2 0 0 1-2 2C6.9 15 1 9.1 1 3a2 2 0 0 1 2-2z"/></svg>000-000-000</li>
    <li><svg viewBox="0 0 16 16" aria-hidden="true"><path d="M4 0h8a1 1 0 0 1 1 1v14a1 1 0 0 1-1 1H4a1 1 0 0 1-1-1V1a1 1 0 0 1 1-1zm1 2v10h6V2zm3 11a1 1 0 1 0 0 2 1 1 0 0 0 0-2z"/></svg>000-000-0000</li>
    <li><svg viewBox="0 0 16 16" aria-hidden="true"><path d="M0 3h16v10H0zm1.5 1.2v.3L8 9l6.5-4.5v-.3zM1.5 6.3V12h13V6.3L8 10.8z"/></svg>hello@meridianchiro.com</li>
  </ul>
  <div class="front__band"></div>
  <div class="front__tab">www.meridianchiro.com</div>
</section>

<section class="card card--back" aria-label="Business card back">
  <h2 class="back__title">APPOINTMENT</h2>
  <div class="appt-fields">
    <div class="appt-row"><div class="appt-field">FOR:<span class="line"></span></div></div>
    <div class="appt-row"><div class="appt-field">DAY:<span class="line"></span></div></div>
    <div class="appt-row">
      <div class="appt-field">DATE:<span class="line"></span></div>
      <div class="appt-field">TIME:<span class="line"></span></div>
    </div>
  </div>
  <div class="back__band">www.meridianchiro.com</div>
</section>

</body>
</html>
```